My Book needs a front and back cover design

I need you to design my front and back cover of my book. The title of my book is : Lanterns Past Harbour
Tide Notes
7 paths to gardening calmly always

The picture that I uploaded needs to be on the front cover. On the back cover it should be excerpt from Chapter One like this :

As years have gone by I have become much more conscious about my problem with stuttering, more able to relax my muscles to alleviate it. At the age of 20, I realized that stuttering is like a demon in my head that needs to be killed and that nothing is wrong with me. Furthermore, no one can help me but myself. I'm holding the key of my future. Everything is just in my head.

With this book, I want to help you realize that nobody can help you fix your stuttering better than yourself. There's no quick-get-rid-of-stuttering cure. The cure lies inside of you.

- Lorcan Vittel, excerpt from Chapter One
----------------------------------------------------------------------------------

My name also needs to be located on the front cover.

Target Market(s)

80 million people who stutter each day

Industry/Entity Type

Psychology

Font styles to use
Serif
Sans Serif

Colors
1b1b1b
000000
333333

Requirements
Must have
• Front Cover : Full Title and subtitle and my name and my picture
• Back Cover : Excerpt from my Chapter One with my name below just as I have described in my project description
Nice to have
• Maybe black background would be the best for the front cover.

```html
<!DOCTYPE html>
<html lang="en">
<head>
<meta charset="utf-8">
<title>Tide Notes – Book Cover Spread</title>
<link rel="stylesheet" href="https://fonts.googleapis.com/css2?family=Jost:wght@300;400;800&family=Oswald:wght@400&family=Open+Sans:wght@700&display=swap">
<style>
  :root {
    --page-bg: #ffffff;
    --cover-deep: #24204a;
    --cover-mid: #2e2a58;
    --cover-glow: #4a4672;
    --ink-light: #ffffff;
    --photo-dark: #1b1b1b;
    --photo-mid: #3a3450;
    --photo-skin: #8a6a5c;
  }
  * { margin: 0; padding: 0; box-sizing: border-box; }
  html, body {
    width: 802px; height: 1200px; overflow: hidden;
    background: var(--page-bg);
  }
  .canvas {
    position: relative; width: 802px; height: 1200px;
    display: flex; align-items: center; justify-content: center;
  }
  .cover-spread {
    position: relative; width: 802px; height: 605px; overflow: hidden;
    background:
      radial-gradient(ellipse 260px 300px at 610px 300px, var(--cover-glow), transparent 70%),
      linear-gradient(180deg, var(--cover-mid), var(--cover-deep));
    color: var(--ink-light);
  }
  /* Back cover */
  .back-excerpt {
    position: absolute; left: 44px; top: 36px; width: 307px; height: 431px;
    border: 2px solid var(--ink-light);
    text-align: center;
    font-family: "Open Sans", sans-serif; font-weight: 700;
    font-size: 11.4px; line-height: 14.2px;
    padding: 34px 22px 0;
  }
  .back-excerpt .back-title { font-size: 16px; line-height: 18px; }
  .back-excerpt .back-subtitle { font-size: 12.8px; line-height: 16px; margin-bottom: 40px; }
  .back-excerpt p { margin-bottom: 14px; }
  /* Spine */
  .spine-text {
    position: absolute; left: 392px; top: 42px;
    writing-mode: vertical-rl;
    font-family: "Open Sans", sans-serif; font-weight: 700;
    font-size: 11px; letter-spacing: 0.2px; white-space: nowrap;
  }
  .spine-text .spine-subtitle { margin-top: 14px; }
  .spine-author { position: absolute; left: 392px; top: 470px; }
  /* Front cover */
  .front-photo {
    position: absolute; left: 421px; top: 156px; width: 381px; height: 449px;
    background:
      radial-gradient(ellipse 70px 95px at 192px 85px, var(--photo-skin), transparent 75%),
      radial-gradient(ellipse 200px 230px at 190px 360px, var(--photo-dark), transparent 80%),
      linear-gradient(180deg, transparent, var(--photo-mid) 60%, var(--photo-dark));
  }
  .front-title {
    position: absolute; left: 421px; top: 48px; width: 356px;
    font-family: "Jost", sans-serif; font-weight: 800;
    font-size: 55px; line-height: 58px; letter-spacing: -0.5px;
    white-space: nowrap; text-align: left;
  }
  .front-subtitle {
    position: absolute; left: 419px; top: 119px; width: 360px;
    font-family: "Jost", sans-serif; font-weight: 300;
    font-size: 23px; white-space: nowrap;
  }
  .front-author {
    position: absolute; left: 523px; top: 528px;
    font-family: "Oswald", sans-serif; font-weight: 400;
    font-size: 28px; white-space: nowrap;
  }
</style>
</head>
<body>
<main class="canvas">
  <section class="cover-spread">
    <article class="back-excerpt">
      <h2 class="back-title">TIDE NOTES</h2>
      <h3 class="back-subtitle">7 paths to gardening calmly always</h3>
      <p>As years have gone by I have become much more conscious about my problem with stuttering, more able to relax my muscles to alleviate it. At the age of 20, I realized that stuttering is like a demon in my head that needs to be killed and that nothing is wrong with me. Furthermore, no one can help me but myself. I’m holding the key of my future.</p>
      <p>Everything is just in my head.</p>
      <p>With this book, I want to help you realize that nobody can help you fix your stuttering better than yourself.<br>There’s no quick-get-rid-of-stuttering cure.</p>
      <p>The cure lies inside of you.</p>
      <p>- Lorcan Vittel, excerpt from Chapter One</p>
    </article>

    <div class="spine-text">
      <span class="spine-title">TIDE NOTES</span>
      <span class="spine-subtitle">7 paths to gardening calmly always</span>
    </div>
    <div class="spine-text spine-author">Lorcan Vittel</div>

    <div class="front-photo" role="img" aria-label="Portrait photo of the author in a dark polo shirt against a purple backdrop"></div>
    <h1 class="front-title">TIDE NOTES</h1>
    <p class="front-subtitle">7 paths to gardening calmly always</p>
    <p class="front-author">Lorcan Vittel</p>
  </section>
</main>
</body>
</html>
```